Medical Marihuana Ziplock Bag Mockup Design

We seek skilled and professional designer for medical marihuana ziplock bag packaging design. We need a modern, minimal, clean Design with the name productname: Plumo - Endproduct will be a ziplock bag (see attachment) samples.
Product may but must not contain a cannabis leaf in Design7Logo

Target Market(s)

young audience

Industry/Entity Type

Medical

Logo Text

P L U M O

Font styles to use
Serif
Sans Serif

Colors
9bcb3c
abd037
cadf82
ffc214
fece3e
fee18a
6b449b
886aae
b8a6cd

Requirements
Nice to have
• Can but must not contain a minimal cannabis leaf as abstract sign

```html
<!DOCTYPE html>
<html lang="en">
<head>
<meta charset="utf-8">
<title>Plumo – Pouch Front</title>
<link rel="stylesheet" href="https://fonts.googleapis.com/css2?family=Montserrat:wght@500;800&display=swap">
<style>
  :root {
    --backdrop: #eeeeee;
    --leaf-green: #5f9620;
    --sun-yellow: #ffc214;
    --paper-white: #ffffff;
    --ink-black: #1d1d1d;
    --logo-cream: #f2efe6;
  }
  html, body {
    margin: 0;
    padding: 0;
    width: 1200px;
    height: 1200px;
    overflow: hidden;
    background: var(--backdrop);
  }
  .canvas {
    position: relative;
    width: 1200px;
    height: 1200px;
  }
  .pouch {
    position: absolute;
    left: 315px;
    top: 150px;
    width: 570px;
    height: 900px;
  }
  .pouch svg { display: block; }
  .brand-name {
    position: absolute;
    left: 0;
    right: 0;
    top: 370px;
    margin: 0;
    text-align: center;
    font-family: "Montserrat", sans-serif;
    font-weight: 800;
    font-size: 132px;
    letter-spacing: -2px;
    color: var(--logo-cream);
    line-height: 1;
  }
  .health-warning {
    position: absolute;
    left: 20px;
    right: 20px;
    top: 602px;
    margin: 0;
    text-align: center;
    font-family: "Montserrat", sans-serif;
    font-weight: 500;
    font-size: 18.5px;
    line-height: 24px;
    color: var(--paper-white);
  }
  .warning-rule {
    position: absolute;
    left: 168px;
    width: 214px;
    height: 2px;
    background: var(--sun-yellow);
  }
  .warning-rule.top { top: 588px; }
  .warning-rule.bottom { top: 760px; }
  .label-box {
    position: absolute;
    background: var(--ink-black);
    color: var(--paper-white);
    font-family: "Montserrat", sans-serif;
    font-weight: 500;
    display: flex;
    align-items: center;
    justify-content: center;
  }
  .label-box.age {
    left: 418px;
    top: 848px;
    width: 46px;
    height: 46px;
    font-size: 12px;
  }
  .label-box.weight {
    left: 467px;
    top: 830px;
    width: 60px;
    height: 60px;
    font-size: 20px;
  }
</style>
</head>
<body>
<main class="canvas">
  <section class="pouch">
    <svg width="570" height="900" viewBox="0 0 570 900">
      <defs>
        <clipPath id="pouch-shape">
          <rect x="0" y="0" width="570" height="900" rx="10" ry="10"/>
        </clipPath>
      </defs>
      <g clip-path="url(#pouch-shape)">
        <rect class="body-green" x="0" y="0" width="570" height="900" fill="var(--leaf-green)"/>
        <polygon class="top-band" role="img" aria-label="Yellow band with fine diagonal stripes"
                 points="0,0 570,0 570,62 0,256" fill="var(--sun-yellow)"/>
        <line x1="0" y1="262" x2="570" y2="66" stroke="var(--paper-white)" stroke-width="9"/>
        <polygon class="bottom-band" role="img" aria-label="Yellow chevron band with fine diagonal stripes"
                 points="0,820 198,888 570,780 570,900 0,900" fill="var(--sun-yellow)"/>
        <polyline points="0,814 198,882 570,774" fill="none" stroke="var(--paper-white)" stroke-width="8"/>
      </g>
    </svg>
    <h1 class="brand-name">Plumo</h1>
    <div class="warning-rule top"></div>
    <p class="health-warning">
      Rauchen fügt Ihnen und den Menschen in<br>
      Ihrer Umgebung erheblichen Schaden zu.<br>
      Fumer nuit gravement à votre santé et à celle<br>
      de votre entourage.<br>
      Il fumo danneggia gravemente<br>
      te e chi ti sta intorno.
    </p>
    <div class="warning-rule bottom"></div>
    <div class="label-box age">18+</div>
    <div class="label-box weight">10g</div>
  </section>
</main>
</body>
</html>
```